New business card/stationary for a consulting company

I am looking for a clean and very professional looking business card for my consulting company as well as corresponding stationary. I am uploading our logo. I like simple and powerful for the feel. No graphics but I am open on everything else. Below is my contact information but would like the final to be in a version I can add my employees information into and print. Thank you.

Daniel Whitcombe
dan@fernlowadvisory.com
2837 North 9th Avenue, Summit Floor, Larkmere, Ohio 60483
www.fernlowadvisory.com

Industry/Entity Type

Consulting

Contact Information for Business Card

Daniel Whitcombe
dan@fernlowadvisory.com
www.fernlowadvisory.com

Font styles to use
Serif
Sans Serif

Requirements
Must have
• Our logo and the business card details.
Nice to have
• our website www.fernlowadvisory.com

```html
<!DOCTYPE html>
<html lang="en">
<head>
<meta charset="utf-8">
<title>Fernlow Advisory – Business Card</title>
<link rel="stylesheet" href="https://fonts.googleapis.com/css2?family=Questrial&family=Montserrat:wght@700&family=Roboto:wght@400&display=swap">
<style>
  :root {
    --backdrop: #dcdcdc;
    --navy: #03035f;
    --card-white: #f2f2f2;
    --band-grey: #a8a8a8;
    --silver: #d6d6d6;
    --text-light: #ffffff;
  }
  * { margin: 0; padding: 0; box-sizing: border-box; }
  html, body { width: 1200px; height: 960px; overflow: hidden; }
  body { background: var(--backdrop); position: relative; }

  .card { position: absolute; width: 600px; height: 342px; overflow: hidden; }

  /* Front side */
  .card-front { left: 302px; top: 130px; background: var(--card-white); }
  .front-mark {
    position: absolute; left: 263px; top: 64px;
    width: 40px; height: 40px; background: var(--navy);
  }
  .front-wordmark {
    position: absolute; left: 0; right: 34px; top: 138px;
    text-align: center; font-family: "Questrial", sans-serif;
    font-size: 31px; letter-spacing: 1.5px; color: var(--navy);
  }
  .name-band {
    position: absolute; left: 0; right: 0; top: 215px; height: 43px;
    background: var(--band-grey); padding-right: 34px;
    display: flex; align-items: center; justify-content: center;
  }
  .person-name {
    font-family: "Montserrat", sans-serif; font-weight: 700;
    font-size: 19px; letter-spacing: 1px; color: var(--navy);
  }
  .contact-band {
    position: absolute; left: 0; right: 0; top: 260px; bottom: 0;
    background: var(--navy); color: var(--text-light);
    font-family: "Roboto", sans-serif; font-size: 15px; line-height: 19px;
    text-align: center; padding-top: 20px; padding-right: 34px;
  }

  /* Back side */
  .card-back { left: 299px; top: 488px; background: var(--navy); }
  .back-mark {
    position: absolute; left: 282px; top: 104px;
    width: 36px; height: 36px; background: var(--silver);
  }
  .back-wordmark {
    position: absolute; left: 0; right: 0; top: 160px;
    text-align: center; font-family: "Questrial", sans-serif;
    font-size: 30px; letter-spacing: 1.5px; color: var(--silver);
  }
  .back-website {
    position: absolute; left: 0; right: 0; top: 285px;
    text-align: center; font-family: "Questrial", sans-serif;
    font-size: 14px; letter-spacing: 4px; color: var(--text-light);
  }
</style>
</head>
<body>
  <section class="card card-front">
    <div class="front-mark"></div>
    <div class="front-wordmark">FERNLOW ADVISORY</div>
    <div class="name-band"><span class="person-name">DANIEL WHITCOMBE</span></div>
    <div class="contact-band">
      <p class="contact-address">2837 North 9th Avenue, Summit Floor, Larkmere, Ohio 60483</p>
      <p class="contact-web">dan@fernlowadvisory.com | www.fernlowadvisory.com</p>
    </div>
  </section>

  <section class="card card-back">
    <div class="back-mark"></div>
    <div class="back-wordmark">FERNLOW ADVISORY</div>
    <div class="back-website">WWW.FERNLOWADVISORY.COM</div>
  </section>
</body>
</html>
```